Website design for learning and development business

I need a logo for my new business based in Australasia. I am a kiwi who is a creative change maker working in the Learning & development space. I design experiential learning opportunities for businesses to grow and nurture their tribes. I take a holistic look at an organisation and analyse what is needed to build a positive culture with a growth mindset woven into their DNA. I would like to see designs that are based on the following word snaps - creative, interesting, tribal, journey, adaptability, engaging, fluid, architectural, bespoke, courageous, challenging .I have the logo (attached) and I Need a startup business website designed. I am a Learning and development professional who is looking at going out on my own and establishing my own business. I would like a website designed that people would go to to check out what I do, how I do, what skills I have and how to contact me. Also room for a blog/articles.

Target Market(s)

Small to medium business

Industry/Entity Type

Self employed training and consultancy company

Number of Pages Required

5+ page

Requirements
Must have
• home page, about page, contact us page, blog page, search for us page
Nice to have
• Testimonials,

```html
<!DOCTYPE html>
<html lang="en">
<head>
<meta charset="utf-8">
<title>Tidewell Consulting</title>
<link href="https://fonts.googleapis.com/css2?family=Lexend+Exa:wght@500;600&family=Montserrat:wght@400;500;600;700&display=swap" rel="stylesheet">
<style>
:root{
  --orange:#ee6a3a;
  --orange-dark:#e0582a;
  --ink:#1d1d1f;
  --text:#3c3c3c;
  --muted:#7a7a7a;
  --blush:#fdf6f2;
  --dark:#1a1a1c;
  --white:#fff;
  --head:"Lexend Exa",sans-serif;
  --body:"Montserrat",sans-serif;
}
*{box-sizing:border-box;margin:0;padding:0}
html,body{width:1200px;height:5324px;overflow:hidden}
body{font-family:var(--body);color:var(--text);background:var(--white);position:relative}
section,header,footer,.block{position:absolute;left:0;width:1200px}
.abs{position:absolute}
.eyebrow{font-size:13px;color:var(--orange);display:flex;align-items:center;gap:10px}
.eyebrow::after{content:"";width:160px;height:1px;background:var(--orange);opacity:.7}
.eyebrow.center::before{content:"";width:80px;height:1px;background:var(--orange);opacity:.7}
.eyebrow.center::after{width:230px}
h2{font-family:var(--head);font-weight:600;font-size:26px;color:var(--ink);line-height:1.6;letter-spacing:.5px}
p{font-size:13px;line-height:23px}
.btn{background:var(--orange);color:#fff;font-size:12px;display:flex;align-items:center;justify-content:center;font-weight:500}
.link{color:var(--orange);font-size:13px;font-weight:600}
.photo{border-radius:0}

/* top bar + nav */
.topbar{top:0;height:37px;background:var(--orange);color:#fff;font-size:12px}
.topbar .phone{left:150px;top:11px;display:flex;gap:8px;align-items:center}
.topbar .mail{right:150px;top:11px;display:flex;gap:8px;align-items:center}
.nav{top:37px;height:60px;background:#fff}
.nav a{position:absolute;top:22px;font-size:13px;color:var(--ink);font-weight:500;text-decoration:none}
.logo-box{position:absolute;left:487px;top:0;width:225px;height:128px;background:#111;z-index:5;display:flex;align-items:center;justify-content:center;gap:10px}
.logo-box span{font-family:var(--body);font-weight:700;color:#fff;font-size:20px;letter-spacing:1px}
.logo-box i{width:12px;height:12px;border-radius:50%;background:var(--orange)}
.nav .cta{left:923px;top:0;width:133px;height:60px;background:#111;color:var(--orange);display:flex;align-items:center;justify-content:center;font-weight:600}

/* hero */
.hero{top:97px;height:523px;background:linear-gradient(160deg,#6d6258,#3b3632 55%,#2c2a26);text-align:center;color:#fff}
.hero h1{position:absolute;top:172px;width:100%;font-family:var(--head);font-weight:600;font-size:34px;letter-spacing:3px}
.hero .sub{position:absolute;top:222px;width:100%;font-size:19px;line-height:33px}
.hero .btn{position:absolute;left:529px;top:306px;width:142px;height:47px}

/* intro */
.intro{top:620px;height:512px;background:var(--blush)}
.intro .frame{left:149px;top:90px;width:450px;height:356px;background:var(--orange)}
.intro .photo{left:166px;top:82px;width:447px;height:340px;background:linear-gradient(135deg,#a47a58,#5f5f63 60%,#3c3d40)}
.stats{left:706px;top:382px;display:flex;gap:60px}
.stats b{display:block;font-family:var(--head);font-size:22px;color:var(--ink);font-weight:600}
.stats small{font-size:11px;color:var(--orange);display:block;margin-top:14px}

/* about */
.about{top:1132px;height:516px}
.about .frame{left:604px;top:100px;width:446px;height:343px;background:var(--orange)}
.about .photo{left:584px;top:84px;width:450px;height:342px;background:linear-gradient(135deg,#8a7d72,#c8c2bc 50%,#6a6763)}

/* services */
.services{top:1648px;height:785px;background:linear-gradient(160deg,#2a2724,#161618)}
.services h2{color:#fff}
.card{position:absolute;width:209px;height:211px;background:#fff;padding:22px}
.card .ico{width:58px;height:50px;background:var(--orange);display:flex;align-items:center;justify-content:center;margin-left:2px;margin-top:2px}
.card.on{background:var(--orange)}
.card.on .ico{background:#fff}
.card h3{font-size:13px;font-weight:600;color:var(--ink);margin-top:26px}
.card p{font-size:11px;line-height:21px;margin-top:12px;color:#555}
.card.on h3,.card.on p{color:#fff}

/* case studies */
.cases{top:2433px;height:902px;background:var(--blush)}
.ticks li{list-style:none;position:relative;padding-left:30px;font-size:13px;line-height:23px}
.ticks li::before{content:"";position:absolute;left:0;top:5px;width:12px;height:12px;border-radius:50%;background:var(--orange)}
.dots{left:512px;top:382px;width:192px;height:48px;background-image:radial-gradient(var(--orange) 2px,transparent 2.5px);background-size:24px 22px}
.case-card{left:597px;top:470px;width:452px;height:286px;background:#fff;box-shadow:0 6px 24px rgba(0,0,0,.08);padding:40px 52px}
.case-card h3{font-family:var(--body);font-size:23px;font-weight:700;color:var(--ink);line-height:36px}
.case-card p{font-size:11px;line-height:21px;color:var(--muted);margin-top:18px}

/* testimonials */
.testi{top:3335px;height:506px;background:#fffbf9}
.quote{position:absolute;width:414px;height:208px;border:2px solid #f1c8b6;border-top-color:var(--orange);border-bottom:2px solid var(--orange);border-left:none;border-right:none;padding:36px 40px}
.quote::before,.quote::after{content:"";position:absolute;top:0;bottom:0;width:2px;background:var(--orange)}
.quote::before{left:0}.quote::after{right:0}
.qmark{position:absolute;top:-26px;left:50px;width:54px;height:50px;background:var(--orange);color:#fff;font-size:44px;font-weight:700;text-align:center;line-height:62px;font-family:var(--head)}
.quote p{font-size:13px;line-height:24px;color:#444}
.who{display:flex;align-items:center;gap:14px;margin-top:20px}
.who .av{width:58px;height:52px;background:linear-gradient(135deg,#b9a89a,#6b5f58)}
.who b{font-size:11px;font-weight:500;color:var(--ink);display:block}
.who small{font-size:11px;color:var(--orange);display:block;margin-top:8px}

/* blog */
.blog{top:3841px;height:677px}
.post{position:absolute;top:153px;width:285px}
.post .img{height:262px}
.post .date{font-size:11px;color:var(--muted);margin-top:18px}
.post h4{font-size:14px;color:var(--orange);font-weight:600;line-height:25px;margin-top:12px}
.post p{font-size:12px;line-height:22px;margin-top:12px}
.post .link{display:block;font-size:11px;margin-top:12px}

/* contact */
.contact{top:4518px;height:479px;background:linear-gradient(160deg,#3b3835,#1e1d1f)}
.contact h2{color:#fff}
.contact p{color:#eee;font-size:12px}
.field{position:absolute;height:35px;background:#fff;font-size:11px;color:#888;padding:11px 22px}

/* footer */
.foot{top:4997px;height:327px;background:linear-gradient(160deg,#2c2b2d,#161618);color:#ccc}
.foot h5{font-size:13px;font-weight:500;color:#fff;letter-spacing:.5px}
.foot .col{position:absolute;top:55px;font-size:11px;line-height:22px}
.brand{font-family:var(--body);font-weight:700;color:#fff;font-size:22px}
.copy{position:absolute;bottom:16px;width:100%;text-align:center;font-size:12px;color:#bbb}
.soc{display:flex;gap:22px;margin-top:14px}
.soc i{width:22px;height:22px;border:1px solid #777;border-radius:50%;display:block}
</style>
</head>
<body>

<header class="topbar">
  <div class="abs phone">
    <svg width="14" height="14" viewBox="0 0 24 24"><path fill="#fff" d="M6.6 10.8a15 15 0 0 0 6.6 6.6l2.2-2.2a1 1 0 0 1 1-.3 11 11 0 0 0 3.6.6 1 1 0 0 1 1 1V20a1 1 0 0 1-1 1A17 17 0 0 1 3 4a1 1 0 0 1 1-1h3.5a1 1 0 0 1 1 1c0 1.3.2 2.5.6 3.6a1 1 0 0 1-.3 1z"/></svg>
    (1800) 555 0199
  </div>
  <div class="abs mail">
    <svg width="16" height="12" viewBox="0 0 16 12"><rect x=".5" y=".5" width="15" height="11" fill="none" stroke="#fff"/><path d="M.5.5 8 7l7.5-6.5" fill="none" stroke="#fff"/></svg>
    hello@tidewell.co
  </div>
</header>

<nav class="nav block">
  <a style="left:150px">Home</a>
  <a style="left:217px">About</a>
  <a style="left:284px">Services</a>
  <a style="left:369px">Blog</a>
  <div class="logo-box"><i></i><span>TIDEWELL</span></div>
  <a style="left:757px">Reviews</a>
  <a style="left:841px">Search</a>
  <a class="cta">CONTACT US</a>
</nav>

<section class="hero" role="img" aria-label="Team meeting around a table in a bright office">
  <h1>DEVELOP YOUR BUSINESS</h1>
  <div class="sub">We are the best L&amp;D experts that helps<br>you to grow your business.</div>
  <div class="btn">GET STARTED</div>
</section>

<section class="intro">
  <div class="abs frame"></div>
  <div class="abs photo" role="img" aria-label="Speaker presenting to a seated group in a brick-walled office"></div>
  <div class="abs eyebrow" style="left:706px;top:76px">Consulting Company</div>
  <h2 class="abs" style="left:706px;top:96px;line-height:41px">Developing People<br>Delivering Results</h2>
  <p class="abs" style="left:706px;top:206px;width:330px">Lorem ipsum dolor sit amet, consetetur sadipscing elitr, sed diam nonumy eirmod tempor invidunt ut labore et dolore magna.</p>
  <p class="abs" style="left:706px;top:292px;width:330px">Aliquyam erat, sed diam voluptua. At vero eos et accusam et justo duo dolores et ea rebum.</p>
  <div class="abs stats">
    <div><b>50</b><small>Expert Staff</small></div>
    <div><b>200+</b><small>Companies</small></div>
    <div><b>2500+</b><small>Happy Clients</small></div>
  </div>
</section>

<section class="about">
  <div class="abs eyebrow" style="left:149px;top:78px">Who we are</div>
  <h2 class="abs" style="left:149px;top:98px;line-height:41px">About Tidewell<br>Consulting</h2>
  <p class="abs" style="left:149px;top:198px;width:400px">Lorem ipsum dolor sit amet, consetetur sadipscing elitr, sed diam nonumy eirmod tempor invidunt ut labore et dolore magna aliquyam erat.</p>
  <p class="abs" style="left:149px;top:286px;width:400px">Sed diam voluptua. At vero eos et accusam et justo duo dolores et ea rebum. Stet clita kasd gub.</p>
  <p class="abs" style="left:149px;top:352px;width:400px">Consetetur sadipscing elitr, sed diam nonumy eirmod. tempor invidunt ut labore et dolore magna.</p>
  <div class="abs link" style="left:149px;top:424px">Know More &rarr;</div>
  <div class="abs frame"></div>
  <div class="abs photo" role="img" aria-label="Two colleagues talking across a desk with a laptop"></div>
</section>

<section class="services">
  <div class="abs eyebrow" style="left:149px;top:78px;color:var(--orange)">We serve the best Services</div>
  <h2 class="abs" style="left:149px;top:100px;color:#fff">Our Services &amp; Features</h2>

  <div class="card" style="left:149px;top:188px"><div class="ico"><svg width="20" height="20" viewBox="0 0 24 24"><path fill="#fff" d="M21 16v-2l-8-5V3.5a1.5 1.5 0 0 0-3 0V9l-8 5v2l8-2.5V19l-2 1.5V22l3.5-1 3.5 1v-1.5L13 19v-5.5z"/></svg></div><h3>Int. Consultation</h3><p>Lorem ipsum dolor sit amet, consetetur sadipscing elitr, sed diam nonumy eirmod</p></div>
  <div class="card" style="left:380px;top:188px"><div class="ico"><svg width="16" height="20" viewBox="0 0 16 20"><path fill="#fff" d="M0 0h10l6 6v14H0z"/><rect x="4" y="9" width="8" height="2" fill="#ee6a3a"/><rect x="4" y="13" width="8" height="2" fill="#ee6a3a"/></svg></div><h3>Tax Consultation</h3><p>Lorem ipsum dolor sit amet, consetetur sadipscing elitr, sed diam nonumy eirmod</p></div>
  <div class="card on" style="left:611px;top:188px"><div class="ico"><span style="color:var(--orange);font-weight:700;font-size:20px">$</span></div><h3>Finance Consultation</h3><p>Lorem ipsum dolor sit amet, consetetur sadipscing elitr, sed diam nonumy eirmod</p></div>
  <div class="card" style="left:842px;top:188px"><div class="ico"><svg width="18" height="20" viewBox="0 0 18 20"><circle cx="9" cy="6" r="5" fill="#fff"/><path fill="#fff" d="M0 20a9 8 0 0 1 18 0z"/></svg></div><h3>Customer Consultation</h3><p>Lorem ipsum dolor sit amet, consetetur sadipscing elitr, sed diam nonumy eirmod</p></div>

  <div class="card" style="left:149px;top:423px"><div class="ico"><svg width="20" height="20" viewBox="0 0 24 24"><path fill="#fff" d="M21 16v-2l-8-5V3.5a1.5 1.5 0 0 0-3 0V9l-8 5v2l8-2.5V19l-2 1.5V22l3.5-1 3.5 1v-1.5L13 19v-5.5z"/></svg></div><h3>Int. Consultation</h3><p>Lorem ipsum dolor sit amet, consetetur sadipscing elitr, sed diam nonumy eirmod</p></div>
  <div class="card" style="left:380px;top:423px"><div class="ico"><svg width="20" height="20" viewBox="0 0 24 24"><path fill="#fff" d="M21 16v-2l-8-5V3.5a1.5 1.5 0 0 0-3 0V9l-8 5v2l8-2.5V19l-2 1.5V22l3.5-1 3.5 1v-1.5L13 19v-5.5z"/></svg></div><h3>Tax Consultation</h3><p>Lorem ipsum dolor sit amet, consetetur sadipscing elitr, sed diam nonumy eirmod</p></div>
  <div class="card" style="left:611px;top:423px"><div class="ico"><svg width="20" height="20" viewBox="0 0 24 24"><path fill="#fff" d="M21 16v-2l-8-5V3.5a1.5 1.5 0 0 0-3 0V9l-8 5v2l8-2.5V19l-2 1.5V22l3.5-1 3.5 1v-1.5L13 19v-5.5z"/></svg></div><h3>Finance Consultation</h3><p>Lorem ipsum dolor sit amet, consetetur sadipscing elitr, sed diam nonumy eirmod</p></div>
  <div class="card" style="left:842px;top:423px"><div class="ico"><svg width="20" height="20" viewBox="0 0 24 24"><path fill="#fff" d="M21 16v-2l-8-5V3.5a1.5 1.5 0 0 0-3 0V9l-8 5v2l8-2.5V19l-2 1.5V22l3.5-1 3.5 1v-1.5L13 19v-5.5z"/></svg></div><h3>Customer Consultation</h3><p>Lorem ipsum dolor sit amet, consetetur sadipscing elitr, sed diam nonumy eirmod</p></div>

  <div class="abs btn" style="left:541px;top:688px;width:118px;height:47px;font-size:13px">View All</div>
</section>

<section class="cases">
  <div class="abs eyebrow" style="left:641px;top:61px">Featured Projects</div>
  <h2 class="abs" style="left:641px;top:80px">Our Recent Case Studies</h2>
  <div class="abs" role="img" aria-label="Illustration of a curled-tail creature filled with an office scene" style="left:149px;top:127px;width:413px;height:145px;background:linear-gradient(90deg,#8b8a88,#d9d5d0 60%,#efe6dc);border-radius:70px 120px 90px 40px"></div>
  <ul class="abs ticks" style="left:644px;top:150px;width:405px">
    <li>Lorem ipsum dolor sit amet, consetetur sadipscing elitr, sed diam nonumy eirmod tempor invidunt ut labore et dolore magna aliquyam erat.</li>
    <li style="margin-top:20px">Sed diam voluptua. At vero eos et accusam et justo duo dolores et ea rebum. Stet clita kasd gub.</li>
    <li style="margin-top:20px">Consetetur sadipscing elitr, sed diam nonumy eirmod. tempor invidunt ut labore et dolore magna.</li>
  </ul>
  <div class="abs dots"></div>
  <div class="abs photo" role="img" aria-label="Team working together at a laptop" style="left:149px;top:450px;width:487px;height:380px;background:linear-gradient(135deg,#7d7570,#c8c0b6 50%,#4a4644)"></div>
  <div class="abs case-card">
    <h3>Helping Kestrel grow their Financing sector.</h3>
    <p>Lorem ipsum dolor sit amet, consectetur adipiscing elit. In purus urna, maximus eu consequat non, sollicitudin nec nisi. Cras non urna quis metus gravida vestibulum sit amet id felis. Aliquam nec libero at mauris dictum efficitur. Praesent</p>
    <div class="btn" style="width:194px;height:42px;margin-top:22px">Read Full Case Study</div>
    <svg class="abs" style="right:30px;bottom:30px" width="54" height="18" viewBox="0 0 54 18"><path d="M10 2 3 9l7 7" fill="none" stroke="#222" stroke-width="2"/><path d="M40 2l7 7-7 7" fill="none" stroke="#ee6a3a" stroke-width="2"/></svg>
  </div>
</section>

<section class="testi">
  <div class="abs eyebrow center" style="left:280px;top:42px;width:640px;justify-content:center">Testimonial</div>
  <h2 class="abs" style="width:100%;text-align:center;top:62px">What our Clients say about Us</h2>
  <div class="quote" style="left:149px;top:186px">
    <div class="qmark">&ldquo;</div>
    <p>Lorem ipsum dolor sit amet, consetetur sadipscing elitr, sed diam nonumy eirmod tempor invidunt ut labore et dolore magna aliquyam erat, sed diam.</p>
    <div class="who"><div class="av" role="img" aria-label="Client portrait"></div><div><b>Aaron Whitby</b><small>CEO of Ironbark</small></div></div>
  </div>
  <div class="quote" style="left:636px;top:186px">
    <div class="qmark">&ldquo;</div>
    <p>Lorem ipsum dolor sit amet, consetetur sadipscing elitr, sed diam nonumy eirmod tempor invidunt ut labore et dolore magna aliquyam erat, sed diam.</p>
    <div class="who"><div class="av" role="img" aria-label="Client portrait"></div><div><b>Mara Kohu</b><small>Senior Developer</small></div></div>
  </div>
  <svg class="abs" style="left:520px;top:432px" width="160" height="20" viewBox="0 0 160 20"><path d="M12 3 5 10l7 7" fill="none" stroke="#222" stroke-width="2"/><circle cx="57" cy="10" r="6" fill="#ee6a3a"/><circle cx="79" cy="10" r="6" fill="none" stroke="#ee6a3a" stroke-width="2"/><circle cx="101" cy="10" r="6" fill="none" stroke="#ee6a3a" stroke-width="2"/><path d="M148 3l7 7-7 7" fill="none" stroke="#ee6a3a" stroke-width="2"/></svg>
</section>

<section class="blog">
  <div class="abs eyebrow" style="width:100%;justify-content:center;top:45px">Our Blog</div>
  <h2 class="abs" style="width:100%;text-align:center;top:70px">Latest News</h2>
  <article class="post" style="left:149px">
    <div class="img" role="img" aria-label="Man working on a laptop at a cafe table" style="background:linear-gradient(135deg,#b9865a,#5c4a3c)"></div>
    <div class="date">July 26, 2021</div>
    <h4>Aliquam nec libero at mauris dictum efficitur.</h4>
    <p>Lorem ipsum dolor sit amet, consectetur adipiscing elit. In purus urna, maximus eu consequat non, sollicitudin nec nisi.</p>
    <span class="link">Read More &rarr;</span>
  </article>
  <article class="post" style="left:456px">
    <div class="img" role="img" aria-label="Open office with round pendant lights and monitors" style="background:linear-gradient(135deg,#e6e9ed,#5b6670 60%,#2f353b)"></div>
    <div class="date">July 26, 2021</div>
    <h4>Aliquam nec libero at mauris dictum efficitur.</h4>
    <p>Lorem ipsum dolor sit amet, consectetur adipiscing elit. In purus urna, maximus eu consequat non, sollicitudin nec nisi.</p>
    <span class="link">Read More &rarr;</span>
  </article>
  <article class="post" style="left:764px">
    <div class="img" role="img" aria-label="Desk with a large monitor in a studio" style="background:linear-gradient(135deg,#d7d3cf,#8c8783 60%,#f0ece8)"></div>
    <div class="date">July 26, 2021</div>
    <h4>Aliquam nec libero at mauris dictum efficitur.</h4>
    <p>Lorem ipsum dolor sit amet, consectetur adipiscing elit. In purus urna, maximus eu consequat non, sollicitudin nec nisi.</p>
    <span class="link">Read More &rarr;</span>
  </article>
</section>

<section class="contact">
  <div class="abs" style="left:149px;top:38px;font-size:13px;color:var(--orange)">Get in Touch</div>
  <h2 class="abs" style="left:149px;top:60px">Contact Us</h2>
  <p class="abs" style="left:149px;top:112px;width:900px;line-height:21px">Would you like to speak to one of our business advisers over the phone? Just submit your details and we'll be in touch shortly. You can  also email us if you would prefer.</p>
  <div class="field" style="left:149px;top:172px;width:440px">Your Name</div>
  <div class="field" style="left:610px;top:172px;width:439px">Email Address</div>
  <div class="field" style="left:149px;top:230px;width:440px">Phone Number</div>
  <div class="field" style="left:610px;top:230px;width:439px">I would like to discuss...<svg class="abs" style="right:22px;top:15px" width="10" height="6" viewBox="0 0 10 6"><path d="M0 0h10L5 6z" fill="#222"/></svg></div>
  <div class="field" style="left:149px;top:289px;width:900px;height:97px">Message</div>
  <div class="abs btn" style="left:828px;top:409px;width:221px;height:35px;font-size:11px">Submit</div>
</section>

<footer class="foot">
  <div class="col" style="left:149px;top:50px;width:200px">
    <div class="brand">Tidewell</div>
    <div style="color:#fff;font-size:12px;margin-top:-2px">Consulting</div>
    <div style="margin-top:18px">Lorem ipsum dolor sit amet, consectetur adipiscing elit.</div>
    <div class="soc"><i></i><i></i><i></i></div>
  </div>
  <div class="col" style="left:403px">
    <h5>COMPANY</h5>
    <div style="margin-top:10px">Home<br>About<br>Services<br>Reviews<br>Blog<br>Contact Us</div>
  </div>
  <div class="col" style="left:582px;width:170px">
    <h5>CONTACT US</h5>
    <div style="margin-top:10px;line-height:17px">
      <div>Call us at:<br>(1800) 555 0199</div>
      <div style="margin-top:16px">Email us at:<br>hello@tidewell.co</div>
      <div style="margin-top:16px">Our Headquarters:<br>48 Harbour Lane</div>
    </div>
  </div>
  <div class="col" style="left:817px;width:232px">
    <h5>NEWSLETTER</h5>
    <div style="margin-top:10px;line-height:17px">Subscribe to our newsletter to<br>Get daily new tips.</div>
    <div style="display:flex;margin-top:18px;height:33px">
      <div style="flex:1;background:#fff;color:#999;font-size:10px;padding:9px 20px">Email Address</div>
      <div class="btn" style="width:86px;font-size:10px">SUBSCRIBE</div>
    </div>
  </div>
  <div class="copy">&copy;2021 Tidewell Consulting | All Rights Reserved</div>
</footer>

</body>
</html>
```